Something that stands out and has more of a modern look to it...will be printing on plastic cards so keep in mind and review old business card as reference

Industry/Entity Type

Real Estate Agent

Contact Information for Business Card

Front of business card will have picture and information the back of card can have logo or name in cursive etc

Logo Text

Marcus Velloran

Font styles to use
Decorative
Script

Colors

Designer to choose colors to be used in the design.

Requirements
Must have
• Must have "Summit 48" logo and state "Bright Harbor Realty Inc Brokerage*" next to it.
• Offices in: Toronto, Markham, Durham
• *Independently Owned and Operated trademarks owned by Summit 48 Real Estate LLC used under license or authorized sub-license. 2017 Summit 48 Canada Limited Partnership. (See old business card for reference)
• Email address: marcus@mvelloranhomes.example
• Website: www.MVelloranHomes.example
• Direct: 647-555-0148
• Name: Marcus Vel Loran
• Office: 905-555-0172
Nice to have
• Maybe a catchy slogan
• One side can have my name designed or the Logo
Should not have
• The Summit 48 Logo too large or focused on (my business requires me just to have this somewhere on the card).
• Yellow and black theme

```html
<!DOCTYPE html>
<html lang="en">
<head>
<meta charset="utf-8">
<title>Marcus Velloran Realty – Business Card</title>
<link href="https://fonts.googleapis.com/css2?family=Cinzel:wght@500&family=Great+Vibes&family=Lato:wght@400;700&display=swap" rel="stylesheet">
<style>
  :root {
    --page-bg: #2b2b2d;
    --card-white: #ffffff;
    --card-dark-top: #2e2c2d;
    --card-dark-bottom: #1c1b1c;
    --ink-dark: #1f1f22;
    --ink-muted: #6b6b70;
    --brand-blue: #2f78c4;
    --text-light: #f2f2f2;
    --text-dim: #a9a9ae;
    --photo-mid: #24324f;
    --photo-blue: #2c5aa0;
  }
  * { box-sizing: border-box; margin: 0; padding: 0; }
  html, body { width: 1200px; height: 852px; overflow: hidden; }
  body {
    background: var(--page-bg);
    position: relative;
    font-family: "Lato", sans-serif;
  }
  .card {
    position: absolute;
    top: 266px;
    width: 540px;
    height: 320px;
    border-radius: 22px;
    overflow: hidden;
    box-shadow: 0 14px 30px rgba(0,0,0,0.45);
  }
  .card--logo { left: 40px; background: var(--card-white); }
  .card--profile {
    left: 620px;
    background: linear-gradient(160deg, var(--card-dark-top), var(--card-dark-bottom));
  }

  /* Logo side */
  .brand {
    position: absolute;
    left: 0; right: 0; top: 78px;
    text-align: center;
  }
  .brand__name {
    font-family: "Great Vibes", cursive;
    font-size: 62px;
    color: var(--ink-dark);
    line-height: 1.05;
  }
  .brand__tag {
    display: flex;
    align-items: center;
    justify-content: center;
    gap: 12px;
    margin-top: 6px;
  }
  .brand__rule { width: 92px; height: 2px; background: var(--brand-blue); }
  .brand__sub {
    font-family: "Cinzel", serif;
    font-size: 15px;
    letter-spacing: 3px;
    color: var(--brand-blue);
  }
  .brokerage {
    position: absolute;
    left: 0; right: 0; top: 232px;
    display: flex;
    align-items: center;
    justify-content: center;
    gap: 8px;
    font-size: 12px;
    color: var(--ink-dark);
  }
  .brokerage__mark { width: 10px; height: 10px; background: var(--ink-dark); }
  .brokerage__name { font-weight: 700; }
  .brokerage__office { color: var(--ink-muted); }
  .disclaimer {
    position: absolute;
    left: 40px; right: 40px; bottom: 18px;
    text-align: center;
    font-size: 8px;
    line-height: 1.35;
    color: var(--ink-muted);
  }

  /* Profile side */
  .portrait {
    position: absolute;
    right: 0; bottom: 0;
    width: 290px; height: 300px;
    background: radial-gradient(ellipse 60% 75% at 60% 100%, var(--photo-blue) 0%, var(--photo-mid) 50%, rgba(36,50,79,0) 100%);
  }
  .agent {
    position: absolute;
    left: 34px; top: 64px;
  }
  .agent__name {
    font-family: "Cinzel", serif;
    font-weight: 500;
    font-size: 30px;
    color: var(--text-light);
    line-height: 1;
  }
  .agent__title {
    font-size: 13px;
    color: var(--brand-blue);
    margin-top: 4px;
    letter-spacing: 0.3px;
  }
  .contacts {
    position: absolute;
    left: 34px; top: 166px;
    list-style: none;
  }
  .contacts li {
    display: flex;
    align-items: center;
    gap: 10px;
    font-size: 13px;
    color: var(--text-light);
    height: 21px;
  }
  .contacts svg { width: 13px; height: 13px; fill: var(--brand-blue); flex: none; }
  .contacts__label { color: var(--text-dim); width: 40px; }
  .offices {
    position: absolute;
    left: 34px; top: 262px;
    font-size: 12.5px;
    line-height: 1.45;
    color: var(--text-light);
  }
</style>
</head>
<body>

<section class="card card--logo" aria-label="Card back with brand name">
  <div class="brand">
    <div class="brand__name">Marcus Velloran</div>
    <div class="brand__tag">
      <span class="brand__rule"></span>
      <span class="brand__sub">REALTY</span>
      <span class="brand__rule"></span>
    </div>
  </div>
  <div class="brokerage">
    <span class="brokerage__mark"></span>
    <span class="brokerage__name">Summit 48</span>
    <span class="brokerage__office">Bright Harbor Realty Inc Brokerage*</span>
  </div>
  <p class="disclaimer">*Independently Owned and Operated trademarks owned by Summit 48 Real Estate LLC used under license or authorized sub-license. 2017 Summit 48 Canada Limited Partnership.</p>
</section>

<section class="card card--profile" aria-label="Card front with agent details">
  <div class="portrait" role="img" aria-label="Portrait photo of the agent in a blue blazer"></div>

  <div class="agent">
    <div class="agent__name">VEL LORAN</div>
    <div class="agent__title">Marcus Vel Loran · Sales Representative</div>
  </div>

  <ul class="contacts">
    <li>
      <svg viewBox="0 0 16 16"><path d="M3 1h3l1.5 4-2 1.3a8 8 0 0 0 4.2 4.2L11 8.5l4 1.5v3a2 2 0 0 1-2 2A12 12 0 0 1 1 3a2 2 0 0 1 2-2z"/></svg>
      <span class="contacts__label">Direct</span> 647-555-0148
    </li>
    <li>
      <svg viewBox="0 0 16 16"><path d="M4 0h8a1 1 0 0 1 1 1v14a1 1 0 0 1-1 1H4a1 1 0 0 1-1-1V1a1 1 0 0 1 1-1zm1 2v10h6V2zm3 11a1 1 0 1 0 0 2 1 1 0 0 0 0-2z"/></svg>
      <span class="contacts__label">Office</span> 905-555-0172
    </li>
    <li>
      <svg viewBox="0 0 16 16"><path d="M1 3h14v10H1zm1.5 1.2v.3L8 8.4l5.5-3.9v-.3z"/></svg>
      marcus@mvelloranhomes.example
    </li>
    <li>
      <svg viewBox="0 0 16 16"><path d="M8 0a8 8 0 1 0 0 16A8 8 0 0 0 8 0zm5.9 7H11a12 12 0 0 0-1-4.7A6 6 0 0 1 13.9 7zM8 2c.8 1 1.4 2.8 1.5 5h-3C6.6 4.8 7.2 3 8 2zM6 2.3A12 12 0 0 0 5 7H2.1A6 6 0 0 1 6 2.3zM2.1 9H5a12 12 0 0 0 1 4.7A6 6 0 0 1 2.1 9zM8 14c-.8-1-1.4-2.8-1.5-5h3c-.1 2.2-.7 4-1.5 5zm2-.3A12 12 0 0 0 11 9h2.9a6 6 0 0 1-3.9 4.7z"/></svg>
      www.MVelloranHomes.example
    </li>
  </ul>

  <div class="offices">Offices in:<br>Toronto · Markham · Durham</div>
</section>

</body>
</html>
```